Business Card Design

we specialise in supply of custom uniforms - teamwear to Schools and sporting clubs, see our website: www.harbourkitcove.com.au, our main corporate colour is black and white, with small amount of gold/yellow

Industry/Entity Type

Business

Contact Information for Business Card

Harbour Kit Cove
Travis Okafor
Ph 03 6218 5097
Mobile 0462 318 740
email: travis@harbourkitcove.com.au
www.harbourkitcove.com.au
like us on facebook

Requirements
Must have
• modern look & feel

```html
<!DOCTYPE html>
<html lang="en">
<head>
<meta charset="utf-8">
<title>Harbour Kit Cove – Business Card</title>
<link rel="stylesheet" href="https://fonts.googleapis.com/css2?family=Arimo:wght@400;700&display=swap">
<style>
  :root {
    --backdrop: #e9e6e1;
    --card-black: #050505;
    --brand-yellow: #fff200;
    --ink-dark: #231f20;
    --text-white: #ffffff;
  }
  * { margin: 0; padding: 0; box-sizing: border-box; }
  html, body {
    width: 1200px;
    height: 1000px;
    overflow: hidden;
    background: var(--backdrop);
    font-family: "Arimo", Arial, sans-serif;
  }
  .business-card {
    position: absolute;
    left: 141px;
    top: 218px;
    width: 918px;
    height: 564px;
    background: var(--card-black);
    box-shadow: 0 6px 14px rgba(0,0,0,0.25);
  }
  .accent-tab {
    position: absolute;
    left: 0;
    top: 232px;
    width: 58px;
    height: 99px;
    background: var(--brand-yellow);
  }
  .brand-name {
    position: absolute;
    left: 96px;
    top: 268px;
    width: 186px;
    color: var(--text-white);
    font-weight: 700;
    font-size: 21px;
    line-height: 1;
    white-space: nowrap;
    letter-spacing: -0.2px;
  }
  .name-band {
    position: absolute;
    left: 286px;
    top: 240px;
    width: 632px;
    height: 104px;
    background: var(--brand-yellow);
  }
  .person-name {
    position: absolute;
    right: 33px;
    top: 24px;
    color: var(--ink-dark);
    font-weight: 700;
    font-size: 50px;
    letter-spacing: -1.5px;
    line-height: 1;
  }
  .contact-list {
    position: absolute;
    right: 14px;
    top: 404px;
    list-style: none;
    text-align: right;
  }
  .contact-item {
    display: flex;
    justify-content: flex-end;
    align-items: center;
    gap: 6px;
    color: var(--text-white);
    font-size: 27px;
    letter-spacing: -1.2px;
    line-height: 32px;
  }
  .contact-icon {
    width: 20px;
    height: 20px;
    flex: none;
  }
  .contact-icon * {
    fill: none;
    stroke: var(--brand-yellow);
    stroke-width: 2;
  }
</style>
</head>
<body>
  <div class="business-card">
    <div class="accent-tab"></div>
    <div class="brand-name">Harbour Kit Cove</div>
    <div class="name-band">
      <div class="person-name">Travis Okafor</div>
    </div>
    <ul class="contact-list">
      <li class="contact-item">03 6218 5097
        <svg class="contact-icon" viewBox="0 0 20 20" aria-hidden="true">
          <rect x="5" y="2" width="10" height="5"/>
          <rect x="2" y="7" width="16" height="7" rx="1"/>
          <rect x="5" y="12" width="10" height="5"/>
        </svg>
      </li>
      <li class="contact-item">0462 318 740
        <svg class="contact-icon" viewBox="0 0 20 20" aria-hidden="true">
          <rect x="6" y="3" width="9" height="15" rx="2"/>
          <line x1="8" y1="7" x2="13" y2="7"/>
        </svg>
      </li>
      <li class="contact-item">travis@harbourkitcove.com.au
        <svg class="contact-icon" viewBox="0 0 20 20" aria-hidden="true">
          <rect x="2" y="5" width="16" height="11"/>
          <polyline points="2,5 10,12 18,5"/>
        </svg>
      </li>
      <li class="contact-item">www.harbourkitcove.com.au
        <svg class="contact-icon" viewBox="0 0 20 20" aria-hidden="true">
          <circle cx="10" cy="10" r="7.5"/>
          <ellipse cx="10" cy="10" rx="3.5" ry="7.5"/>
          <line x1="2.5" y1="10" x2="17.5" y2="10"/>
        </svg>
      </li>
    </ul>
  </div>
</body>
</html>
```